Business Card Professional Clean - Lumavault

Create a business card for my company that deals with Cryptocurrencies. I have a few designs ideas that I'd like to be implemented. Thanks! I will include the logo files, and a link to the design styles that I like.

Target Market(s)

Professionals

Industry/Entity Type

Consulting

Contact Information for Business Card

Name: Mark Dunn
Title: CEO/Technical Director
Phone: (587)943-0586
E-mail: mdunn@lumavault.ca
Address: Suite 512, 208-3370 Harwood Avenue NW

Twitter: @LumaVaultHQ
Instagram: lumavaulthq

Colors
92b5d7
3276b5
33a6d7
85acd3
85cae6
0592cd

Requirements
Must have
• Some colors that match with the logo and the pictures I put in below.
• Ideally the finished product would look something like the attachments showing the color gradient I want.
Nice to have
• Please see some of the attachments I've included. This is very close to the final product that I would like to see. If someone could recreate something like those I would definitely feel pretty good about it.
• For the instagram and twitter please use the symbols/icon to represent it on the card.
Should not have
• No crazy colors and unprofessional styles. I just want clear info. Don't go outside the boundaries of the colors in the attachment and we should be good. No crazy weird fonts either.

```html
<!DOCTYPE html>
<html lang="en">
<head>
<meta charset="utf-8">
<title>Lumavault Business Card</title>
<link rel="stylesheet" href="https://fonts.googleapis.com/css2?family=Montserrat:wght@400;500;800&display=swap">
<style>
  :root {
    --page: #2a2d31;
    --card-dark: #1f2830;
    --card-dark-2: #2a343e;
    --panel-light: #eef0f2;
    --panel-light-2: #d6d9dc;
    --ink: #1f2830;
    --brand-deep: #3276b5;
    --brand-mid: #0592cd;
    --brand-bright: #33a6d7;
    --band-1: #85cae6;
    --band-2: #92b5d7;
    --band-3: #33a6d7;
    --band-4: #3276b5;
  }
  * { box-sizing: border-box; margin: 0; padding: 0; }
  html, body { width: 1200px; height: 900px; overflow: hidden; }
  body {
    background: var(--page);
    font-family: "Montserrat", sans-serif;
    display: flex;
    align-items: center;
    justify-content: center;
    gap: 60px;
  }
  .card {
    position: relative;
    width: 540px;
    height: 310px;
    border-radius: 22px;
    overflow: hidden;
    background: var(--card-dark);
  }

  /* ---------- front ---------- */
  .card-front .edge-strip { position: absolute; inset: 0; }
  .light-panel {
    position: absolute;
    left: 0; top: 0;
    width: 270px; height: 310px;
    background: radial-gradient(circle at 40% 35%, var(--panel-light), var(--panel-light-2));
  }
  .identity {
    position: absolute;
    left: 42px; top: 70px;
    width: 210px;
  }
  .brand-word {
    display: flex;
    align-items: center;
    gap: 8px;
    font-weight: 500;
    font-size: 17px;
    color: var(--ink);
    margin-bottom: 24px;
  }
  .brand-mark {
    width: 16px; height: 16px;
    border: 2px solid var(--brand-deep);
  }
  .person-name {
    font-weight: 800;
    font-size: 27px;
    letter-spacing: 0.5px;
    color: var(--brand-deep);
    line-height: 1;
  }
  .person-title {
    margin-top: 6px;
    font-size: 12px;
    color: var(--ink);
  }
  .contact-list { position: absolute; inset: 0; list-style: none; }
  .contact-row {
    position: absolute;
    display: flex;
    align-items: center;
    gap: 14px;
    padding-left: 30px;
    font-size: 12.5px;
    color: var(--ink);
  }
  .contact-row svg { width: 16px; height: 16px; flex: none; fill: var(--ink); }
  .row-phone   { left: 250px; top: 30px;  width: 250px; height: 58px; background: var(--band-1); border-radius: 18px 0 0 0; }
  .row-email   { left: 250px; top: 88px;  width: 250px; height: 56px; background: var(--band-2); }
  .row-web     { left: 250px; top: 144px; width: 250px; height: 56px; background: var(--band-3); }
  .row-address { left: 250px; top: 200px; width: 250px; height: 76px; background: var(--band-4); line-height: 1.35; border-radius: 0 0 0 18px; }

  /* ---------- back ---------- */
  .card-back { background: linear-gradient(160deg, var(--card-dark-2), var(--card-dark)); }
  .card-back .edge-accent { position: absolute; inset: 0; }
  .back-brand {
    position: absolute;
    inset: 0;
    display: flex;
    align-items: center;
    justify-content: center;
    gap: 14px;
    font-weight: 500;
    font-size: 40px;
    letter-spacing: 2px;
    color: var(--brand-deep);
  }
  .back-brand .brand-mark { width: 26px; height: 26px; border-width: 3px; }
  .social-dot {
    position: absolute;
    width: 14px; height: 14px;
    border-radius: 50%;
    background: #e8ecef;
  }
  .social-twitter   { left: 30px; top: 26px; }
  .social-instagram { right: 30px; bottom: 26px; }
</style>
</head>
<body>

  <section class="card card-front" aria-label="Business card front">
    <div class="light-panel"></div>
    <svg class="edge-strip" viewBox="0 0 540 310" aria-hidden="true">
      <defs>
        <linearGradient id="stripBlue" x1="0" y1="0" x2="0" y2="1">
          <stop offset="0" stop-color="#3276b5"/>
          <stop offset="1" stop-color="#0592cd"/>
        </linearGradient>
      </defs>
      <path d="M0 0 H18 V40 Q18 50 26 54 Q32 58 32 68 V242 Q32 252 26 256 Q18 260 18 270 V310 H0 Z" fill="url(#stripBlue)"/>
    </svg>
    <div class="identity">
      <div class="brand-word"><span class="brand-mark"></span>Lumavault</div>
      <h1 class="person-name">MARK DUNN</h1>
      <p class="person-title">CEO/Technical Director</p>
    </div>
    <ul class="contact-list">
      <li class="contact-row row-phone">
        <svg viewBox="0 0 24 24"><path d="M6.6 10.8a15 15 0 0 0 6.6 6.6l2.2-2.2a1 1 0 0 1 1-.25 11.4 11.4 0 0 0 3.6.57 1 1 0 0 1 1 1V20a1 1 0 0 1-1 1A17 17 0 0 1 3 4a1 1 0 0 1 1-1h3.5a1 1 0 0 1 1 1c0 1.25.2 2.45.57 3.57a1 1 0 0 1-.25 1z"/></svg>
        (587)943-0586
      </li>
      <li class="contact-row row-email">
        <svg viewBox="0 0 24 24"><path d="M2 5h20v14H2z M2 5l10 8 10-8" fill="none" stroke="#1f2830" stroke-width="2"/></svg>
        mdunn@lumavault.ca
      </li>
      <li class="contact-row row-web">
        <svg viewBox="0 0 24 24"><g fill="none" stroke="#1f2830" stroke-width="1.8"><circle cx="12" cy="12" r="9"/><ellipse cx="12" cy="12" rx="4" ry="9"/><path d="M3 12h18M5 7h14M5 17h14"/></g></svg>
        www.lumavault.ca
      </li>
      <li class="contact-row row-address">
        <svg viewBox="0 0 24 24"><path d="M12 2a7 7 0 0 0-7 7c0 5 7 13 7 13s7-8 7-13a7 7 0 0 0-7-7zm0 9.5A2.5 2.5 0 1 1 12 6.5a2.5 2.5 0 0 1 0 5z"/></svg>
        <span>Suite 512, 208-3370<br>Harwood Avenue NW</span>
      </li>
    </ul>
  </section>

  <section class="card card-back" aria-label="Business card back">
    <svg class="edge-accent" viewBox="0 0 540 310" aria-hidden="true">
      <path d="M0 0 H120 Q108 0 104 8 Q100 18 88 18 H18 V80 Q18 92 8 96 Q0 100 0 112 Z" fill="#0592cd"/>
      <path d="M540 310 H420 Q432 310 436 302 Q440 292 452 292 H522 V230 Q522 218 532 214 Q540 210 540 198 Z" fill="#0592cd"/>
    </svg>
    <span class="social-dot social-twitter"></span>
    <div class="back-brand"><span class="brand-mark"></span>Lumavault</div>
    <span class="social-dot social-instagram"></span>
  </section>

</body>
</html>
```